Business Cards

Business card design for my company.
I would like the card's background colour to be black. You can also see our web site to get an idea of our brand. https://www.tmwhomecrafting.com.au/
- Name
- Email

```html
<!DOCTYPE html>
<html lang="en">
<head>
<meta charset="utf-8">
<title>TMW Home Crafting — Business Cards</title>
<link rel="stylesheet" href="https://fonts.googleapis.com/css2?family=Arimo:wght@400;700&display=swap">
<style>
  :root {
    --bg: #e4e4e4;
    --card-dark: #323232;
    --brand-green: #0d9646;
    --text-light: #f4f4f4;
    --rule: #9a9a9a;
    --card-w: 688px;
    --card-h: 393px;
  }
  * { box-sizing: border-box; margin: 0; padding: 0; }
  html, body { width: 1200px; height: 1200px; overflow: hidden; }
  body {
    background: var(--bg);
    font-family: "Arimo", Arial, sans-serif;
    position: relative;
  }
  .card {
    position: absolute;
    left: 264px;
    width: var(--card-w);
    height: var(--card-h);
    overflow: hidden;
  }
  .card--front { top: 158px; background: var(--card-dark); }
  .card--back  { top: 653px; background: var(--brand-green); }

  .wordmark {
    position: absolute;
    display: flex;
    align-items: center;
    gap: 12px;
    color: var(--text-light);
    font-weight: 700;
    letter-spacing: 0.04em;
    line-height: 1.1;
  }
  .wordmark__square { background: var(--brand-green); flex: none; }
  .card--front .wordmark { right: 48px; top: 70px; font-size: 30px; }
  .card--front .wordmark__square { width: 26px; height: 26px; }
  .card--back .wordmark { left: 50%; top: 50%; transform: translate(-50%, -50%); font-size: 46px; }
  .card--back .wordmark__square { width: 40px; height: 40px; background: var(--card-dark); }

  .holder { position: absolute; left: 48px; top: 222px; }
  .holder__name {
    color: var(--brand-green);
    font-size: 27px;
    font-weight: 700;
    letter-spacing: 0.01em;
    line-height: 1;
  }
  .holder__title { color: var(--text-light); font-size: 15px; margin-top: 6px; }

  .divider {
    position: absolute;
    left: 48px; right: 47px; top: 281px;
    height: 1px; background: var(--rule);
  }

  .contact-list {
    position: absolute; left: 45px; top: 291px;
    list-style: none;
  }
  .contact-list li {
    display: flex; align-items: center; gap: 9px;
    color: var(--text-light); font-size: 16px; height: 20.5px;
  }
  .contact-list svg { width: 15px; height: 15px; fill: var(--brand-green); flex: none; }

  .address {
    position: absolute; right: 43px; top: 293px;
    text-align: right; color: var(--text-light);
    font-size: 16px; line-height: 20.5px; font-style: normal;
  }

  .edge-band { position: absolute; bottom: 0; height: 16px; }
  .edge-band--green { left: 0; width: 419px; background: var(--brand-green); }
  .edge-band--white { left: 423px; right: 0; background: #ffffff; }
</style>
</head>
<body>
  <section class="card card--front" aria-label="Business card front">
    <div class="wordmark">
      <span class="wordmark__square"></span>
      <span>TMW<br>HOME CRAFTING</span>
    </div>

    <div class="holder">
      <p class="holder__name">DANIEL REYES</p>
      <p class="holder__title">President</p>
    </div>

    <div class="divider"></div>

    <ul class="contact-list">
      <li>
        <svg viewBox="0 0 24 24" aria-hidden="true"><path d="M6.6 10.8a15.1 15.1 0 0 0 6.6 6.6l2.2-2.2c.3-.3.7-.4 1-.2 1.1.4 2.3.6 3.6.6.6 0 1 .4 1 1V20c0 .6-.4 1-1 1A17 17 0 0 1 3 4c0-.6.4-1 1-1h3.5c.6 0 1 .4 1 1 0 1.3.2 2.5.6 3.6.1.3 0 .7-.2 1z"/></svg>
        736-555-0142
      </li>
      <li>
        <svg viewBox="0 0 24 24" aria-hidden="true"><path d="M7 1h10a2 2 0 0 1 2 2v18a2 2 0 0 1-2 2H7a2 2 0 0 1-2-2V3a2 2 0 0 1 2-2zm0 3v15h10V4z"/></svg>
        736-555-0187
      </li>
      <li>
        <svg viewBox="0 0 24 24" aria-hidden="true"><path d="M2 5h20v14H2zm2 2v.5l8 5 8-5V7zm0 2.8V17h16V9.8l-8 5z"/></svg>
        info@tmwhome.com
      </li>
    </ul>

    <address class="address">
      1420 Juniper Road<br>
      Fairview, Canada 30218<br>
      www.tmwhome.com
    </address>

    <div class="edge-band edge-band--green"></div>
    <div class="edge-band edge-band--white"></div>
  </section>

  <section class="card card--back" aria-label="Business card back">
    <div class="wordmark">
      <span class="wordmark__square"></span>
      <span>TMW<br>HOME CRAFTING</span>
    </div>
  </section>
</body>
</html>
```